Potential SF Gazette Best Seller Poetry Book Cover Contest

I’m penning my first poetry book. It’s entitled “Lanterns Under Rain”
I’m fairly open to creative freedom but I want the cover to without a doubt catch a persons' eye instantly because first impressions are VERY IMPORTANT in the literary world
I tend to lean towards a luxury look and colors like black, gold, rose gold, silver, glitter etc but again I’m open to interpretation
Looking forward to your submissions
Target Market(s)
those seeking relatable love advice and quotes
modern millenials
Colors
Look and feel

```html
<!DOCTYPE html>
<html lang="en">
<head>
<meta charset="utf-8">
<title>Lanterns Under Rain — Book Cover</title>
<link rel="stylesheet" href="https://fonts.googleapis.com/css2?family=Nunito:wght@900&family=Oswald:wght@600&display=swap">
<style>
  :root {
    --ink-black: #000000;
    --heart-red: #e31e24;
    --heart-red-deep: #b5121a;
    --snow-white: #ffffff;
  }
  html, body {
    margin: 0;
    padding: 0;
    overflow: hidden;
    background: var(--ink-black);
  }
  .cover {
    position: relative;
    width: 750px;
    height: 1200px;
    overflow: hidden;
    background: var(--ink-black);
  }
  .cover-art {
    position: absolute;
    inset: 0;
    width: 750px;
    height: 1200px;
    display: block;
  }
  .title {
    position: absolute;
    top: 178px;
    left: 0;
    width: 750px;
    margin: 0;
    text-align: center;
    font-family: "Nunito", sans-serif;
    font-weight: 900;
    font-size: 98px;
    line-height: 108px;
    letter-spacing: -1px;
    color: var(--snow-white);
    text-transform: uppercase;
  }
  .title span { display: block; }
  .author {
    position: absolute;
    top: 1132px;
    left: 0;
    width: 750px;
    margin: 0;
    text-align: center;
    font-family: "Oswald", sans-serif;
    font-weight: 600;
    font-size: 34px;
    line-height: 44px;
    letter-spacing: 0.5px;
    color: var(--snow-white);
    text-transform: uppercase;
  }
</style>
</head>
<body>
  <main class="cover">
    <svg class="cover-art" viewBox="0 0 750 1200" xmlns="http://www.w3.org/2000/svg">
      <defs>
        <radialGradient id="heart-fill" cx="50%" cy="70%" r="70%">
          <stop offset="0%" stop-color="var(--heart-red)"/>
          <stop offset="100%" stop-color="var(--heart-red-deep)"/>
        </radialGradient>
      </defs>

      <!-- horizon band -->
      <rect class="horizon-band" x="0" y="716" width="750" height="72" fill="var(--snow-white)"/>

      <!-- lower red field -->
      <rect class="lower-field" x="0" y="788" width="750" height="412" fill="var(--heart-red)"/>

      <!-- black path widening downwards -->
      <path class="lower-path" fill="var(--ink-black)"
        d="M375,788 C390,870 410,905 520,975 C650,1058 720,1110 760,1150 L760,1200 L-10,1200 L-10,1150
           C30,1110 100,1058 230,975 C340,905 360,870 375,788 Z"/>

      <!-- heart of branches -->
      <path class="branch-heart" role="img" aria-label="Tangled red tree branches growing together into a heart shape"
        fill="url(#heart-fill)"
        d="M375,788 C345,660 170,610 55,520 C-25,455 -25,220 55,130 C130,50 300,50 375,165
           C450,50 620,50 695,130 C775,220 775,455 695,520 C580,610 405,660 375,788 Z"/>
    </svg>

    <h1 class="title">
      <span>Lanterns</span>
      <span>Under</span>
      <span>Rain</span>
    </h1>

    <p class="author">Morgan Ellery-Vance</p>
  </main>
</body>
</html>
```